Meadow Paws Label

We have basically a start up business that I need help with. This project is just for the label design.

Our product is a frozen raw pet food that promotes weight control, less shedding, smaller stools and an overall better health. The product is in nugget form similar to what you would see in a steak shish kabob. I only share that with you in case you want to incorporate that in the design.

We have been in business for 17 years but all of our sales have been word of mouth. We are going to be launching an infomercial this summer and I need everything stated previously to be completed before we can launch the infomercial.

We need a label created for our first frozen dog food produce. We need the label to say Meadow Paws of course. The label also needs to have the following:

The label needs to be 4 inches x 6 inches.

Combination Diet - Large Font
Ingredients: Beef hearts, beef kidneys, beef tripe, beef liver, chicken necks, chicken mdm, breed premix, broccoli, bone meal, apples, carrots, oystershell, cod liver oil

DATE PACKED: XXXX
LOT #XXXX

BEST IF USED BY: XX-XX-XX

KEEP FROZEN

NET WT. 5 LBS.

```html
<!DOCTYPE html>
<html lang="en">
<head>
<meta charset="utf-8">
<title>Meadow Paws – Combination Diet Label</title>
<link rel="stylesheet" href="https://fonts.googleapis.com/css2?family=League+Gothic&family=Oswald:wght@400;500;600;700&family=Ubuntu:wght@500&display=swap">
<style>
  :root {
    --backdrop: #ececec;
    --label-cream: #fdeee2;
    --ink: #111111;
    --paper-white: #ffffff;
  }
  * { margin: 0; padding: 0; box-sizing: border-box; }
  html, body {
    width: 1200px;
    height: 806px;
    overflow: hidden;
    background: var(--backdrop);
  }
  .label {
    position: absolute;
    left: 350px;
    top: 28px;
    width: 500px;
    height: 750px;
    background: var(--label-cream);
    color: var(--ink);
    font-family: "Oswald", sans-serif;
  }
  .brand-name {
    position: absolute;
    left: 0;
    top: 120px;
    width: 100%;
    text-align: center;
    font-family: "Oswald", sans-serif;
    font-weight: 500;
    font-size: 64px;
    line-height: 1;
    color: var(--ink);
  }
  .tagline-ribbon {
    position: absolute;
    left: 28px;
    top: 240px;
    width: 444px;
    height: 80px;
  }
  .tagline-ribbon text {
    font-family: "Ubuntu", sans-serif;
    font-weight: 500;
    font-size: 17px;
    letter-spacing: 2.2px;
    fill: var(--paper-white);
  }
  .product-title {
    position: absolute;
    left: 0;
    top: 338px;
    width: 100%;
    text-align: center;
    white-space: nowrap;
    font-family: "League Gothic", sans-serif;
    font-weight: 400;
    font-size: 90px;
    line-height: 1;
    letter-spacing: 0.5px;
  }
  .ingredients {
    position: absolute;
    left: 65px;
    top: 440px;
    width: 370px;
  }
  .ingredients-heading {
    text-align: center;
    font-weight: 600;
    font-size: 19px;
    line-height: 30px;
    margin-bottom: 2px;
  }
  .ingredients-list {
    font-weight: 400;
    font-size: 18px;
    line-height: 34px;
  }
  .ingredients-line {
    display: block;
    white-space: nowrap;
    text-align: justify;
    text-align-last: justify;
  }
  .ingredients-line.is-last { text-align-last: center; }
  .storage-note,
  .net-weight {
    position: absolute;
    top: 636px;
    font-weight: 600;
    font-size: 23px;
    line-height: 36px;
    letter-spacing: -0.6px;
  }
  .storage-note { left: 45px; }
  .net-weight { right: 48px; }
  .date-band {
    position: absolute;
    left: 0;
    bottom: 0;
    width: 100%;
    height: 66px;
    background: var(--ink);
    color: var(--paper-white);
    display: flex;
    justify-content: space-between;
    align-items: center;
    padding: 0 48px 0 45px;
    font-weight: 600;
    font-size: 15px;
    letter-spacing: -0.5px;
    white-space: nowrap;
  }
</style>
</head>
<body>
  <main class="label">
    <h1 class="brand-name">Meadow Paws</h1>

    <svg class="tagline-ribbon" viewBox="0 0 444 80" aria-label="100% natural raw dog food">
      <path d="M0 40 L46 24 L46 66 Z" fill="#111111"/>
      <path d="M444 40 L398 24 L398 66 Z" fill="#111111"/>
      <path d="M22 18 Q222 -6 422 18 L422 56 Q222 32 22 56 Z" fill="#111111"/>
      <path id="ribbon-curve" d="M40 44 Q222 20 404 44" fill="none"/>
      <text text-anchor="middle"><textPath href="#ribbon-curve" startOffset="50%">100% NATURAL RAW DOG FOOD</textPath></text>
    </svg>

    <h2 class="product-title">COMBINATION DIET</h2>

    <section class="ingredients">
      <h3 class="ingredients-heading">INGREDIENTS</h3>
      <p class="ingredients-list">
        <span class="ingredients-line">Beef hearts, beef kidneys, beef tripe, beef liver,</span>
        <span class="ingredients-line">chicken necks, chicken mdm, breed premix,</span>
        <span class="ingredients-line">broccoli, bone meal, apples, carrots,</span>
        <span class="ingredients-line is-last">oystershell, cod liver oil</span>
      </p>
    </section>

    <p class="storage-note">KEEP FROZEN</p>
    <p class="net-weight">NET WT. 5 LBS</p>

    <footer class="date-band">
      <span class="best-by">BEST IF USED BY: XX-XX-XX</span>
      <span class="lot-number">LOT #XXXX</span>
      <span class="date-packed">DATE PACKED: XXXX</span>
    </footer>
  </main>
</body>
</html>
```